Web Design for a Biotech Consulting Firm

We need a web site design for a new business based in Philadelphia called VorentaMx. This is a consulting firm that will serve medical diagnostics industry, which is part of the life science/healthcare industry focusing on developing and marketing products that help in early detection, monitoring or management of diseases. Our consulting firm will help medical diagnostic companies to overcome key challenges in designing, evaluating and marketing new products.Our company name is VorentaMx. Vorenta is Latin word for "something" Dx represents diagnostics. The idea behind the name is that we help companies to transform the original, early product ideas ("nothing") into "something"; which is a product with full clinical utility that will help to improve health and well-being.The web site should use the visual feel of the logo (attached), be modern, simple and clean looking and represent creativity, innovation, scientific thinking and progress.
Updates

Wix Design is acceptable

Industry/Entity Type

Biotechnology

Coding

Coded - Design and coding required

Number of Pages Required

1 page

Font styles to use
Sans Serif

Requirements
Must have
• simple, clean look couple of pages
Should not have
• a lot of pages

```html
<!DOCTYPE html>
<html lang="en">
<head>
<meta charset="utf-8">
<title>Vorenta Mx – Pharma and Biotech Consulting</title>
<link href="https://fonts.googleapis.com/css2?family=Poppins:wght@300;400;500;600&family=Roboto+Slab:wght@500&display=swap" rel="stylesheet">
<style>
:root{
  --blue:#1b7ff0;
  --blue-dark:#1468cc;
  --ink:#111;
  --text:#333;
  --grey-bg:#f4f4f4;
  --white:#fff;
}
*{margin:0;padding:0;box-sizing:border-box}
html,body{width:1200px;height:2786px;overflow:hidden}
body{font-family:'Poppins',sans-serif;color:var(--text);background:var(--white);position:relative}
.accent{color:var(--blue)}

/* header */
.site-header{position:absolute;top:0;left:0;width:1200px;height:152px;background:var(--white)}
.brand{position:absolute;left:121px;top:52px;display:flex;align-items:center;gap:12px;font-size:26px;font-weight:400;color:var(--ink);line-height:1;white-space:nowrap}
.brand-mark{width:18px;height:18px;background:var(--blue);flex:none}
.contact-line{position:absolute;top:28px;font-size:17px;font-weight:500;color:var(--ink);display:flex;align-items:center;gap:12px;white-space:nowrap}
.main-nav{position:absolute;top:100px;left:553px;font-size:14.5px;color:var(--ink)}
.main-nav a{text-decoration:none;color:inherit;position:absolute;white-space:nowrap}
.main-nav .current{color:var(--blue)}

/* hero */
.hero{position:absolute;top:152px;left:0;width:1200px;height:491px;overflow:hidden;
  background:linear-gradient(90deg,#050805 0%,#0a1408 30%,#1f4f10 48%,#6d9a1a 60%,#e0a21a 72%,#e23b12 85%,#c21a10 100%)}
.hero-art{position:absolute;inset:0;
  background:radial-gradient(ellipse 300px 200px at 40% 20%,rgba(40,140,30,.45),transparent 70%),
             radial-gradient(ellipse 320px 260px at 82% 60%,rgba(255,60,20,.55),transparent 70%),
             radial-gradient(ellipse 260px 200px at 75% 20%,rgba(255,190,30,.5),transparent 70%)}
.hero h1{position:absolute;left:120px;top:118px;font-size:35px;font-weight:400;color:var(--white);line-height:40px;white-space:nowrap}
.hero p{position:absolute;left:122px;top:206px;width:450px;font-size:15px;line-height:22px;color:var(--white)}
.hero .more{position:absolute;left:122px;top:286px;font-size:14.5px;color:var(--blue);text-decoration:none}
.slide-arrow{position:absolute;top:232px;width:30px;height:26px;background:#333;display:flex;align-items:center;justify-content:center}

/* section shared */
.section-title{position:absolute;left:0;width:1200px;text-align:center;font-size:31px;font-weight:400;color:var(--ink);line-height:1.2}
.section-lead{position:absolute;left:0;width:1200px;text-align:center;font-size:15px;line-height:26px;color:var(--ink)}
.feature{position:absolute;width:290px;text-align:center}
.feature-icon{width:100px;height:100px;border-radius:50%;border:3px solid var(--blue);margin:0 auto;background:radial-gradient(circle at 50% 40%,#fff,#e4e4e4);display:flex;align-items:center;justify-content:center;position:relative}
.feature-icon::after{content:"";position:absolute;bottom:-14px;left:15px;width:70px;height:6px;border-radius:50%;background:rgba(0,0,0,.08)}
.feature h3{font-family:'Roboto Slab',serif;font-weight:500;font-size:15px;color:var(--ink);margin-top:24px}
.feature p{font-size:13px;line-height:24px;color:var(--text);margin-top:8px}
.cta{position:absolute;font-size:16px;font-weight:500;color:var(--ink);text-decoration:none;padding:16px 0 0 22px;height:48px;width:200px;white-space:nowrap}
.cta::before{content:"";position:absolute;left:0;top:0;width:44px;height:46px;border:2px solid var(--blue);border-right:none}

/* about */
.about{position:absolute;top:1220px;left:0;width:1200px;height:633px;background:var(--grey-bg)}
.about h2{position:absolute;left:121px;top:112px;font-size:35px;font-weight:400;color:var(--ink);line-height:1.2}
.about .copy{position:absolute;left:121px;top:172px;width:445px;font-size:13.5px;line-height:24px;color:var(--text)}
.about .copy p+p{margin-top:8px}
.about-frame{position:absolute;left:661px;top:78px;width:446px;height:448px;border-top:6px solid var(--blue);border-right:6px solid var(--blue)}
.about-frame-gap{position:absolute;left:1098px;top:220px;width:14px;height:160px;background:var(--grey-bg)}
.about-photo{position:absolute;left:605px;top:104px;width:472px;height:449px;background:linear-gradient(135deg,#e9eef0 0%,#b9c6cc 40%,#6d7f88 70%,#3b4a52 100%)}

/* footer */
.site-footer{position:absolute;top:2394px;left:0;width:1200px;height:392px;background:var(--blue);color:var(--white)}
.footer-brand{position:absolute;left:0;top:80px;width:1200px;display:flex;justify-content:center;align-items:center;gap:10px;font-size:22px;font-weight:400;line-height:1}
.footer-brand .brand-mark{width:14px;height:14px;background:var(--white)}
.social{position:absolute;top:168px;width:28px;height:28px;border:2px solid var(--white);background:var(--blue-dark)}
.footer-nav a{position:absolute;top:216px;font-size:14.5px;color:var(--white);text-decoration:none;white-space:nowrap}
.footer-box{position:absolute;left:394px;top:264px;width:412px;height:70px;border:1px solid rgba(255,255,255,.7);background:var(--blue-dark);text-align:center;font-size:16px;line-height:23px;padding-top:12px}
.copyright{position:absolute;top:352px;left:0;width:1200px;text-align:center;font-size:11.5px}
.copyright small{font-size:10px}
</style>
</head>
<body>

<header class="site-header">
  <div class="brand"><span class="brand-mark"></span>Vorenta Mx</div>

  <div class="contact-line" style="left:656px">
    <svg width="24" height="24" viewBox="0 0 24 24" fill="none" stroke="#1b7ff0" stroke-width="1.8"><path d="M5 3h4l2 5-2.5 1.5a11 11 0 0 0 6 6L16 13l5 2v4a2 2 0 0 1-2 2A16 16 0 0 1 3 5a2 2 0 0 1 2-2z"/></svg>
    123.456.7890
  </div>
  <div class="contact-line" style="left:854px">
    <svg width="24" height="20" viewBox="0 0 24 20" fill="none" stroke="#1b7ff0" stroke-width="1.8"><rect x="2" y="3" width="20" height="14"/><path d="M2 3l10 8 10-8"/></svg>
    inquiry@vorentamx.com
  </div>

  <nav class="main-nav">
    <a class="current" style="left:0">Home</a>
    <a style="left:87px">About Us</a>
    <a style="left:193px">Our Services</a>
    <a style="left:326px">Resources</a>
    <a style="left:441px">Contact Us</a>
  </nav>
</header>

<section class="hero">
  <div class="hero-art" role="img" aria-label="Swirling green, yellow and red ink clouds on a dark background"></div>
  <h1>Pharma And Biotech Experts<br>For Your Success</h1>
  <p>We are redefining pharmaceutical and biotech consulting by focusing scarce knowledge and proven experience precisely on your goals.</p>
  <a class="more">Click Here To Learn More</a>
  <div class="slide-arrow" style="left:6px"><svg width="10" height="12" viewBox="0 0 10 12"><path d="M7 1L2 6l5 5" stroke="#fff" stroke-width="2" fill="none"/></svg></div>
  <div class="slide-arrow" style="left:1164px"><svg width="10" height="12" viewBox="0 0 10 12"><path d="M3 1l5 5-5 5" stroke="#fff" stroke-width="2" fill="none"/></svg></div>
</section>

<section class="services">
  <h2 class="section-title" style="top:708px">Our <span class="accent">Services</span></h2>
  <p class="section-lead" style="top:761px">Our consulting firm will help medical diagnostic companies to overcome key challenges in</p>

  <div class="feature" style="left:113px;top:827px">
    <div class="feature-icon">
      <svg width="54" height="40" viewBox="0 0 54 40" fill="none" stroke="#111" stroke-width="2.4"><path d="M4 30C16 30 20 10 30 10s14 20 20 20"/><path d="M4 10c12 0 16 20 26 20s14-20 20-20"/><path d="M12 13v14M22 16v8M38 16v8M45 13v14" stroke-width="1.6"/></svg>
    </div>
    <h3>Designing</h3>
    <p>Lorem ipsum dolor sit amet, sectetuer adipiscin ga mortis nisl aliquip fdafe ea commodo consequat. ....[+]</p>
  </div>

  <div class="feature" style="left:453px;top:827px">
    <div class="feature-icon">
      <svg width="48" height="48" viewBox="0 0 48 48" fill="none" stroke="#111" stroke-width="2.6"><rect x="6" y="6" width="32" height="36"/><path d="M12 16h20M12 24h14M12 32h10"/><path d="M42 14L26 34l-4 2 1-5 16-19z" fill="#fff"/></svg>
    </div>
    <h3>Evaluating</h3>
    <p>Lorem ipsum dolor sit amet, sectetuer adipiscin ga mortis nisl aliquip fdafe ea commodo consequat. ....[+]</p>
  </div>

  <div class="feature" style="left:793px;top:827px">
    <div class="feature-icon">
      <svg width="48" height="50" viewBox="0 0 48 50" fill="none" stroke="#111" stroke-width="2.4"><rect x="6" y="4" width="34" height="26"/><path d="M12 12h10M12 18h14M28 10h6v8h-6z"/><path d="M20 48V30a3 3 0 0 1 6 0v8l8 2v8"/></svg>
    </div>
    <h3>Marketing New Products</h3>
    <p>Lorem ipsum dolor sit amet, sectetuer adipiscin ga mortis nisl aliquip fdafe ea commodo consequat. ....[+]</p>
  </div>

  <a class="cta" style="left:514px;top:1098px">Contact Us Today</a>
</section>

<section class="about">
  <h2>About Vorenta <span class="accent">Mx</span></h2>
  <div class="copy">
    <p>Lorem ipsum dolor sit amet, consectetuer adipiscing e, sed diam nonummy nibh euismod tincidunt ut laoreet dolore ma aliquam erat volutpat.</p>
    <p>Lorem ipsum dolor sit amet, consectetuer adipiscing e, sed diam nonummy nibh euismod tincidunt ut laoreet dolore ma aliquam erat volutpat. Ut wisi enim ad minim veniam, quis nostrud exerci tation ullamcorper suscipit lobortis nisl ut aliquip ex ea commodo consequat. Duis autem vel eum iriure dolor in hendrerivulputate velit esse molestie consequat, vel illum dolore eu feugiat nulla facilisis at vero eros et accumsan et iusto odio dissim qui blandit proesent luptatum zzril delenit augue.</p>
  </div>
  <a class="cta" style="left:121px;top:464px">Read More</a>
  <div class="about-frame"></div>
  <div class="about-frame-gap"></div>
  <div class="about-photo" role="img" aria-label="Team meeting in a bright glass-walled office with a presenter at a screen"></div>
</section>

<section class="leader">
  <h2 class="section-title" style="top:1920px">Industry Leader – <span class="accent">Pharmaceutical &amp; Biotech Consulting</span></h2>
  <p class="section-lead" style="top:1974px">We are a full service pharmaceutical and biotech consulting firm that specializes in new product planning and<br>commercial expertise to optimize product launches and brand performance.</p>

  <div class="feature" style="left:119px;top:2048px">
    <div class="feature-icon" role="img" aria-label="Puzzle pieces photo" style="background:radial-gradient(circle,#d8cfb8,#6d6a60)"></div>
    <h3>Explore Our Capabilities</h3>
    <p>Learn how our customized services can<br>help you meet your brand goals.</p>
  </div>
  <div class="feature" style="left:455px;top:2048px">
    <div class="feature-icon" role="img" aria-label="Laptop showing a blog page" style="background:radial-gradient(circle,#f2f2f2,#8fa3b8)"></div>
    <h3>Hear Our Perspectives</h3>
    <p>Lorem ipsum dolor sit amet, sectetuer<br>adipiscin ga mortis nisl aliquip.</p>
  </div>
  <div class="feature" style="left:776px;top:2048px">
    <div class="feature-icon" role="img" aria-label="Keyboard with a contact key" style="background:radial-gradient(circle,#f07a3a,#3f86d8)"></div>
    <h3>Get In Touch</h3>
    <p>Contact us to learn how Vorenta Mx<br>can help your organization.</p>
  </div>

  <a class="cta" style="left:516px;top:2292px">Contact Us Today</a>
</section>

<footer class="site-footer">
  <div class="footer-brand"><span class="brand-mark"></span>Vorenta Mx</div>
  <div class="social" style="left:549px"></div>
  <div class="social" style="left:586px"></div>
  <div class="social" style="left:623px"></div>
  <nav class="footer-nav">
    <a style="left:339px">Home</a>
    <a style="left:424px">About Us</a>
    <a style="left:531px">Our Services</a>
    <a style="left:663px">Resources</a>
    <a style="left:777px">Contact Us</a>
  </nav>
  <div class="footer-box">Contact Us To Learn<br>About How We Can Help Support Your Needs.</div>
  <p class="copyright">Copyright © 2019 Vorenta Mx. All Rights Reserved. <small>Terms of Use | Privacy Policy</small></p>
</footer>

</body>
</html>
```